Bridal show post card design

our company contracts hotels near airports and cruise ports. We sell hotel packages including one night stay at a hotel (before or after the trip) including parking while they are away and transfers to and from the airport or cruise port. we are marketing to the public for the first time (typically it's travel agents). Specifically doing a Bridal show. Below are the photos that will appear in our booth or on our banners etc. We would like a post card to reflect the stress of not booking a hotel with us ... instead they could start their honeymoon or vacation a day early, stay at the hotel and relax... avoiding the stress of getting to the airport or cruise port in time otherwise missing the boat or the flight. We would also like to include a $20 off savings on the post card.
Industry/Entity Type
Hotel

```html
<!DOCTYPE html>
<html lang="en">
<head>
<meta charset="utf-8">
<title>Harbor Stay &amp; Park – Bridal Show Postcard</title>
<link href="https://fonts.googleapis.com/css2?family=Roboto+Condensed:wght@400;700&family=Roboto:wght@400;500&family=Lato:wght@400;700&display=swap" rel="stylesheet">
<style>
  :root {
    --navy: #2f3257;
    --green: #3e9e3a;
    --green-light: #5cbf4f;
    --ink: #222428;
    --white: #ffffff;
    --page: #e4e4e4;
    --frame: #9a9a9a;
  }
  * { margin: 0; padding: 0; box-sizing: border-box; }
  html, body { width: 806px; height: 1200px; overflow: hidden; }
  body { background: var(--page); position: relative; font-family: "Roboto", Arial, sans-serif; }

  .card {
    position: absolute; left: 66px; width: 676px; height: 523px;
    background: var(--white); overflow: hidden;
    box-shadow: 0 4px 14px rgba(0,0,0,0.25);
  }
  .card--front { top: 56px; }
  .card--back { top: 622px; }
  .card__shapes { position: absolute; inset: 0; width: 676px; height: 523px; }
  .card__text { position: absolute; white-space: nowrap; }

  /* front */
  .brand { left: 28px; top: 34px; text-align: center; }
  .brand__name { font-family: "Roboto Condensed", Arial, sans-serif; font-weight: 700; font-size: 30px; color: var(--navy); line-height: 1; }
  .brand__phone { font-family: "Lato", Arial, sans-serif; font-size: 11px; color: var(--green); margin-top: 8px; letter-spacing: .5px; }

  .headline { left: 24px; top: 258px; font-family: "Roboto Condensed", Arial, sans-serif; font-weight: 700; font-size: 52px; color: var(--ink); line-height: 1; }
  .subline { left: 24px; top: 326px; font-size: 19px; color: var(--white); line-height: 27px; }
  .early__lead { left: 24px; top: 396px; font-family: "Roboto Condensed", Arial, sans-serif; font-weight: 700; font-size: 27px; color: var(--green); line-height: 1; }
  .early__tail { left: 24px; top: 430px; font-family: "Lato", Arial, sans-serif; font-weight: 700; font-size: 19px; color: var(--ink); line-height: 1; }
  .call { left: 24px; top: 472px; font-family: "Lato", Arial, sans-serif; font-weight: 700; font-size: 22px; color: var(--white); }
  .call__number { color: var(--navy); }

  .offer { left: 350px; top: 271px; width: 140px; text-align: center; font-family: "Roboto Condensed", Arial, sans-serif; font-weight: 700; line-height: 1; }
  .offer__word { font-size: 38px; color: var(--white); margin-top: 14px; }
  .offer__amount { font-size: 44px; color: var(--green-light); margin-top: 4px; }

  .contact { font-family: "Lato", Arial, sans-serif; font-weight: 700; display: flex; align-items: center; gap: 6px; }
  .contact svg { flex: none; }
  .contact--front { left: 404px; font-size: 19px; color: var(--ink); }
  .contact--front.contact--mail { top: 455px; }
  .contact--front.contact--web { top: 483px; }

  /* back */
  .back__title { left: 22px; top: 192px; font-size: 26px; color: var(--white); letter-spacing: .3px; }
  .about-tag { left: 24px; top: 249px; font-family: "Roboto Condensed", Arial, sans-serif; font-weight: 700; font-size: 21px; color: var(--navy); }
  .about-copy {
    position: absolute; left: 25px; top: 292px; width: 272px;
    font-size: 16.5px; line-height: 22px; color: var(--navy);
    text-align: justify; hyphens: auto;
  }
  .contact--back { left: 26px; font-size: 16px; color: var(--white); }
  .contact--back.contact--mail { top: 470px; }
  .contact--back.contact--web { top: 492px; }

  .stamp { position: absolute; left: 571px; top: 34px; width: 68px; height: 91px; border: 1px solid var(--frame); }
</style>
</head>
<body>

<section class="card card--front">
  <svg class="card__shapes" viewBox="0 0 676 523" aria-hidden="true">
    <defs>
      <linearGradient id="bandGrey" x1="0" x2="1" y1="0" y2="0">
        <stop offset="0" stop-color="#ffffff"/>
        <stop offset="1" stop-color="#cfcfcf"/>
      </linearGradient>
      <linearGradient id="photoStress" x1="0" x2="1" y1="0" y2="1">
        <stop offset="0" stop-color="#e9efe4"/>
        <stop offset=".5" stop-color="#d9cfc6"/>
        <stop offset="1" stop-color="#3a3b42"/>
      </linearGradient>
      <linearGradient id="photoBeach" x1="0" x2="0" y1="0" y2="1">
        <stop offset="0" stop-color="#2f7fc0"/>
        <stop offset=".45" stop-color="#4fc0c8"/>
        <stop offset=".7" stop-color="#e8ddc9"/>
        <stop offset="1" stop-color="#b89c7a"/>
      </linearGradient>
    </defs>
    <polygon points="0,158 228,158 345,0 676,0 676,40 360,318 0,246" fill="url(#photoStress)" role="img" aria-label="Photo: a stressed bride resting her chin on her hands while a groom in a suit looks away"/>
    <polygon points="0,0 345,0 228,158 0,158" fill="var(--white)"/>
    <polyline points="0,155 226,155 340,0" fill="none" stroke="var(--green)" stroke-width="6"/>
    <polygon points="370,322 676,62 676,448 512,384" fill="url(#photoBeach)" role="img" aria-label="Photo: a couple walking hand in hand onto a tropical beach beside a wooden lounger"/>
    <polygon points="352,312 676,40 676,62 370,322" fill="var(--navy)"/>
    <polygon points="505,378 676,440 676,452 500,388" fill="var(--navy)"/>
    <polygon points="0,238 198,238 482,384 470,396 196,250 0,250" fill="var(--navy)"/>
    <polygon points="0,250 196,250 470,396 395,523 0,523" fill="var(--green)"/>
    <polygon points="0,394 341,394 312,458 0,458" fill="url(#bandGrey)"/>
    <polygon points="372,448 676,448 676,523 345,523" fill="url(#bandGrey)"/>
    <polygon transform="translate(420,341)" fill="var(--navy)" points="70,0 62.2,9.8 66.6,21.6 56.1,28.6 56.6,41.2 44.5,44.5 41.2,56.6 28.6,56.1 21.6,66.6 9.8,62.2 0,70 -9.8,62.2 -21.6,66.6 -28.6,56.1 -41.2,56.6 -44.5,44.5 -56.6,41.2 -56.1,28.6 -66.6,21.6 -62.2,9.8 -70,0 -62.2,-9.8 -66.6,-21.6 -56.1,-28.6 -56.6,-41.2 -44.5,-44.5 -41.2,-56.6 -28.6,-56.1 -21.6,-66.6 -9.8,-62.2 0,-70 9.8,-62.2 21.6,-66.6 28.6,-56.1 41.2,-56.6 44.5,-44.5 56.6,-41.2 56.1,-28.6 66.6,-21.6 62.2,-9.8"/>
  </svg>

  <div class="card__text brand">
    <div class="brand__name">Harbor Stay &amp; Park</div>
    <div class="brand__phone">800-555-0142</div>
  </div>

  <div class="card__text headline">STRESS!</div>
  <div class="card__text subline">OF NOT BOOKING<br>A HOTEL WITH US</div>
  <div class="card__text early__lead">Instead you could start</div>
  <div class="card__text early__tail">Your vacation a day early</div>
  <div class="card__text call">Call now <span class="call__number">800-555-0142</span></div>

  <div class="card__text offer">
    <div class="offer__word">Save</div>
    <div class="offer__amount">20%</div>
  </div>

  <div class="card__text contact contact--front contact--mail">
    <svg width="14" height="10" viewBox="0 0 14 10" aria-hidden="true"><rect width="14" height="10" fill="var(--green)"/><polyline points="0,0 7,6 14,0" fill="none" stroke="var(--white)" stroke-width="1.2"/></svg>
    info@harborstaypark.com
  </div>
  <div class="card__text contact contact--front contact--web">
    <svg width="13" height="13" viewBox="0 0 13 13" aria-hidden="true"><circle cx="6.5" cy="6.5" r="6.5" fill="var(--green)"/><path d="M0 6.5h13M6.5 0c-3 3-3 10 0 13M6.5 0c3 3 3 10 0 13" fill="none" stroke="var(--white)" stroke-width=".9"/></svg>
    www.harborstaypark.com
  </div>
</section>

<section class="card card--back">
  <svg class="card__shapes" viewBox="0 0 676 523" aria-hidden="true">
    <defs>
      <linearGradient id="sand" x1="0" x2="1" y1="0" y2="1">
        <stop offset="0" stop-color="#c9ab86"/>
        <stop offset="1" stop-color="#a98762"/>
      </linearGradient>
      <linearGradient id="greenPanel" x1="0" x2="1" y1="0" y2="0">
        <stop offset="0" stop-color="#3e9e3a"/>
        <stop offset="1" stop-color="#4cb043"/>
      </linearGradient>
      <linearGradient id="tagGrey" x1="0" x2="1" y1="0" y2="0">
        <stop offset="0" stop-color="#ffffff"/>
        <stop offset="1" stop-color="#d0d0d0"/>
      </linearGradient>
    </defs>
    <polygon points="0,0 358,0 347,161 0,161" fill="url(#sand)" role="img" aria-label="Photo: the word Relax written by hand in beach sand"/>
    <polygon points="0,166 340,166 322,456 0,456" fill="url(#greenPanel)"/>
    <polygon points="340,166 346,166 328,456 322,456" fill="var(--white)"/>
    <polygon points="360,0 376,0 344,456 340,523 326,523 330,456" fill="var(--navy)"/>
    <polygon points="0,456 342,456 340,523 0,523" fill="var(--navy)"/>
    <polygon points="0,245 137,245 124,273 0,273" fill="url(#tagGrey)"/>
  </svg>

  <div class="stamp"></div>

  <div class="card__text back__title">AVOID YOUR STRESS</div>
  <div class="card__text about-tag">ABOUT US</div>
  <p class="about-copy">We sell hotel packages including one night stay at a hotel (before or after the trip) including parking while they are away and transfers to and from the airport or cruise port.</p>

  <div class="card__text contact contact--back contact--mail">
    <svg width="13" height="9" viewBox="0 0 14 10" aria-hidden="true"><rect width="14" height="10" fill="var(--green)"/><polyline points="0,0 7,6 14,0" fill="none" stroke="var(--navy)" stroke-width="1.2"/></svg>
    info@harborstaypark.com
  </div>
  <div class="card__text contact contact--back contact--web">
    <svg width="12" height="12" viewBox="0 0 13 13" aria-hidden="true"><circle cx="6.5" cy="6.5" r="6.5" fill="var(--green)"/><path d="M0 6.5h13M6.5 0c-3 3-3 10 0 13M6.5 0c3 3 3 10 0 13" fill="none" stroke="var(--navy)" stroke-width=".9"/></svg>
    www.harborstaypark.com
  </div>
</section>

</body>
</html>
```